Web Design for ORV Air conditioning company

Hello,

I am calling on you for the modernization of the company's website
https://clim-solaris-atelier.fr/

The new one must include the new logo with the new graphic charter (color, style ...)

I'm looking for a simple design (less is more), a font written without Serif, the logo that brings a touch of color and modernity.

(maintenance and installation company for air conditioning and ventilation systems)
COLORS: in line with the logo

CHAPTER:

# PRESENTATION
# SERVICES
AIR CONDITIONING (ice cube icon)
HEATING (flame icon)
AIR TREATMENT (icon fan)
# ACHIEVEMENTS

# CONTACT
CONTACT FORM
GOOGLE MAPS

Target Market(s)

Showcase site for our customers

Coding

Coded - Design and coding required

Number of Pages Required

4 page

Font styles to use
Sans Serif

Colors
33b8a4
33a6d7
3176b5
ffffff

Requirements
Must have
• Clear and fluid navigation
a visual identity of the page with the logo
Should not have
• Overloaded.

```html
<!DOCTYPE html>
<html lang="en">
<head>
<meta charset="utf-8">
<title>ORV — Clim Solaris Atelier</title>
<link href="https://fonts.googleapis.com/css2?family=Montserrat:wght@400;500;600;700;800&display=swap" rel="stylesheet">
<style>
:root{
  --blue:#2a8fc4;
  --green:#3ec88e;
  --teal:#33b8a4;
  --navy:#1f3a6e;
  --ink:#1d2733;
  --dark:#2c3a48;
  --text:#4b5563;
  --line:#b9bec4;
  --light:#f2f3f4;
  --white:#ffffff;
  --grad:linear-gradient(90deg,var(--blue),var(--green));
}
*{margin:0;padding:0;box-sizing:border-box}
html,body{width:1200px;height:3264px;overflow:hidden}
body{position:relative;font-family:'Montserrat',sans-serif;background:var(--white);color:var(--ink)}
.abs{position:absolute}
.center{text-align:center}

/* header */
.header{left:0;top:0;width:1200px;height:93px;background:var(--white)}
.brand{left:76px;top:16px;display:flex;align-items:flex-start;gap:6px}
.logo{font-weight:800;font-size:38px;line-height:46px;color:var(--teal)}
.logo-sq{width:8px;height:8px;background:var(--teal);margin-top:6px}
.tagline{left:184px;top:46px;font-size:12px;font-weight:600;color:#6b7a88;white-space:nowrap}
.nav a{position:absolute;top:37px;font-size:15px;font-weight:700;color:var(--blue);text-decoration:none;transform:translateX(-50%);white-space:nowrap}
.nav a.active{color:var(--ink)}
.nav-underline{left:497px;top:62px;width:34px;height:3px;background:var(--green);border-radius:2px}
.phone{left:962px;top:33px;font-size:18px;font-weight:700;color:var(--ink);display:flex;align-items:center;gap:6px}

/* hero */
.hero-photo{left:0;top:93px;width:1200px;height:693px;background:radial-gradient(ellipse at 30% 30%,#3a3d42,#222428 70%)}
.hero-title{left:0;top:278px;width:1200px;font-size:44px;font-weight:800;line-height:45px;color:var(--white)}
.hero-sub{left:0;top:388px;width:1200px;font-size:19px;font-weight:500;color:var(--white)}
.btn{display:flex;align-items:center;justify-content:center;background:var(--grad);color:var(--white);font-weight:700;border-radius:30px;text-transform:uppercase}
.hero-ring{left:492px;top:437px;width:207px;height:59px;border:2px solid #cfd3d6;border-radius:32px}
.hero-btn{left:500px;top:444px;width:191px;height:45px;font-size:14px}
.hero-edge{left:0;top:640px}

/* about */
.sec-title{font-size:32px;font-weight:800;color:var(--ink);text-transform:uppercase}
.underline{height:2px;background:var(--grad)}
.about-title{left:0;top:852px;width:1200px}
.about-line{left:564px;top:898px;width:63px}
.about-text{left:195px;top:932px;width:810px;font-size:18px;line-height:35px;color:var(--text)}
.about-btn{left:500px;top:1094px;width:193px;height:48px;font-size:14px}

/* stats */
.stat{top:1208px;width:240px;transform:translateX(-50%)}
.stat-num{font-size:50px;font-weight:800;color:var(--navy);line-height:58px}
.stat-label{font-size:20px;font-weight:500;color:var(--blue);margin-top:6px}
.divider{top:1216px;width:2px;height:84px;background:#d8dbde}

/* services */
.services{left:0;top:1324px;width:1200px;height:621px;background:linear-gradient(90deg,#2a93c2,#3bc38f 60%,#3ec88e)}
.services-title{left:0;top:1480px;width:1200px;color:var(--white)}
.services-line{left:572px;top:1526px;width:63px;background:var(--white)}
.card{top:1575px;width:327px;height:269px;border:2px solid rgba(255,255,255,.85);color:var(--white)}
.card.featured{border:none;background:linear-gradient(180deg,#3b4a5a,#26323e);box-shadow:0 16px 30px rgba(0,0,0,.25)}
.card-icon{position:absolute;left:50%;top:34px;transform:translateX(-50%)}
.card-title{position:absolute;left:0;top:120px;width:100%;font-size:21px;font-weight:800}
.card-text{position:absolute;left:30px;top:152px;width:calc(100% - 60px);font-size:13.5px;line-height:20px;font-weight:500}
.card-arrow{position:absolute;left:50%;bottom:-24px;transform:translateX(-50%);width:46px;height:46px;border-radius:50%;background:var(--teal);border:2px solid var(--white);display:flex;align-items:center;justify-content:center}

/* quote */
.quote-photo{left:0;top:1945px;width:597px;height:551px;background:linear-gradient(160deg,#4a5866,#9fa9b3 40%,#e5e8ea 70%,#7d8894)}
.quote-title{left:687px;top:2002px;font-size:28px}
.quote-line{left:687px;top:2047px;width:46px}
.field{left:687px;width:422px;border:1px solid var(--line);font-size:12px;color:var(--ink);padding:0 21px;display:flex;align-items:center}
.field.area{align-items:flex-start;padding-top:18px}
.submit{left:690px;top:2379px;width:193px;height:48px;font-size:15px}

/* contact */
.contact-bg{left:0;top:2496px;width:1200px;height:500px;background:linear-gradient(90deg,#f3f3f3,#f7f7f7 50%,#fafafa)}
.contact-title{left:128px;top:2596px;font-size:28px}
.contact-line{left:128px;top:2641px;width:63px}
.info{left:168px;font-size:17px;line-height:29px;color:var(--ink)}
.info-icon{left:132px}
.map{left:536px;top:2587px;width:570px;height:327px;background:linear-gradient(135deg,#eef0f2,#e4e7ea);border:1px solid #e0e2e4}

/* footer */
.footer{left:0;top:2980px;width:1200px;height:284px}
.footer-logo{left:0;top:3050px;width:1200px;font-size:44px;font-weight:800;color:var(--green);letter-spacing:2px}
.fnav a{position:absolute;top:3128px;transform:translateX(-50%);font-size:16px;font-weight:700;color:var(--white);text-decoration:none;white-space:nowrap}
.copyright{left:0;top:3167px;width:1200px;font-size:13px;color:#a8b0b8}
.social{top:3210px;width:30px;height:30px;border-radius:50%;border:2px solid var(--white)}
.social.first{border-color:var(--green)}
</style>
</head>
<body>

<header class="abs header">
  <div class="abs brand"><span class="logo">ORV</span><span class="logo-sq"></span></div>
  <div class="abs tagline">CLIM SOLARIS ATELIER</div>
  <nav class="nav">
    <a class="active" style="left:514px">HOME</a>
    <a style="left:613px">ABOUT</a>
    <a style="left:725px">SERVICES</a>
    <a style="left:861px">CONTACT US</a>
  </nav>
  <div class="abs nav-underline"></div>
  <div class="abs phone">
    <svg width="20" height="20" viewBox="0 0 24 24"><path fill="#2a8fc4" d="M6.6 10.8a15.2 15.2 0 0 0 6.6 6.6l2.2-2.2a1 1 0 0 1 1-.25 11.4 11.4 0 0 0 3.6.57 1 1 0 0 1 1 1V20a1 1 0 0 1-1 1A17 17 0 0 1 3 4a1 1 0 0 1 1-1h3.5a1 1 0 0 1 1 1c0 1.25.2 2.45.57 3.57a1 1 0 0 1-.25 1z"/></svg>
    123 555 0190
  </div>
</header>

<section>
  <div class="abs hero-photo" role="img" aria-label="Dark workbench background scattered with plumbing parts, wrenches, pliers and work gloves"></div>
  <h1 class="abs hero-title center">CLIM SOLARIS ATELIER<br>VALMORAY</h1>
  <p class="abs hero-sub center">LA SOLUTION A VOTRE PROBLÈME DE MAINTENANCE</p>
  <div class="abs hero-ring"></div>
  <div class="abs btn hero-btn">Request a quote</div>
  <svg class="abs hero-edge" width="1200" height="146" viewBox="0 0 1200 146">
    <defs><linearGradient id="edgeGrad" x1="0" x2="1"><stop offset="0" stop-color="#2a8fc4"/><stop offset="1" stop-color="#3ec88e"/></linearGradient></defs>
    <polygon points="70,22 600,146 1130,18 600,112" fill="url(#edgeGrad)"/>
    <polygon points="0,10 600,150 1200,10 1200,146 0,146" fill="#ffffff"/>
  </svg>
</section>

<section>
  <h2 class="abs sec-title about-title center">About ORV</h2>
  <div class="abs underline about-line"></div>
  <p class="abs about-text center">Lorem ipsum dolor sit amet, consectetur adipiscing elit, sed do eiusmod tempor incididunt ut labore et dolore magna aliqua. Ut enim ad minim veniam, quis nostrud exercitation ullamco laboris nisi ut aliquip ex ea commodo consequat. Duis aute irure dolor in reprehenderit in voluptate velit esse cillum dolore eu fugiat nulla pariatur.</p>
  <div class="abs btn about-btn">Request a quote</div>

  <div class="abs stat center" style="left:204px"><div class="stat-num">07</div><div class="stat-label">CLIENTS</div></div>
  <div class="abs divider" style="left:314px"></div>
  <div class="abs stat center" style="left:437px"><div class="stat-num">650</div><div class="stat-label">CONTRACT</div></div>
  <div class="abs divider" style="left:556px"></div>
  <div class="abs stat center" style="left:688px"><div class="stat-num">590</div><div class="stat-label">SATISFIED</div></div>
  <div class="abs divider" style="left:796px"></div>
  <div class="abs stat center" style="left:945px"><div class="stat-num">1752</div><div class="stat-label">STOCK PRODUCTS</div></div>
</section>

<section>
  <div class="abs services">
    <svg width="1200" height="112" viewBox="0 0 1200 112">
      <polygon points="40,18 600,112 1160,12 600,94" fill="#2c3a48"/>
      <polygon points="0,0 1200,0 1200,0 600,96 0,0" fill="#ffffff"/>
    </svg>
  </div>
  <h2 class="abs sec-title services-title center">Our Services</h2>
  <div class="abs underline services-line"></div>

  <div class="abs card center" style="left:92px">
    <svg class="card-icon" width="84" height="70" viewBox="0 0 84 70" fill="none" stroke="#fff" stroke-width="2.4" stroke-linejoin="round">
      <rect x="30" y="4" width="24" height="24" rx="2"/><rect x="12" y="30" width="26" height="28" rx="2"/><rect x="44" y="30" width="26" height="28" rx="2"/><path d="M4 64h76"/>
    </svg>
    <div class="card-title">AIR CONDITIONING</div>
    <div class="card-text">Auis nostrud exercitation ullamco laboris nisi ut aliquip ex ea commodo consequat. Duis aute</div>
    <div class="card-arrow"><svg width="16" height="10" viewBox="0 0 16 10"><path d="M2 2l6 6 6-6" stroke="#fff" stroke-width="2.6" fill="none"/></svg></div>
  </div>

  <div class="abs card featured center" style="left:441px" role="img" aria-label="Heating service card over a dim photo of wall-mounted outdoor units">
    <svg class="card-icon" width="60" height="70" viewBox="0 0 60 70" fill="none" stroke="#fff" stroke-width="2.4" stroke-linejoin="round">
      <path d="M30 4c4 14 22 20 22 40a22 22 0 0 1-44 0c0-10 6-16 10-20 0 8 4 12 8 12-4-14 2-24 4-32z"/><path d="M30 40c2 6 10 8 10 16a10 10 0 0 1-20 0c0-6 6-8 10-16z"/>
    </svg>
    <div class="card-title">HEATING</div>
    <div class="card-text">Auis nostrud exercitation ullamco laboris nisi ut aliquip ex ea commodo consequat. Duis aute</div>
    <div class="card-arrow"><svg width="16" height="10" viewBox="0 0 16 10"><path d="M2 2l6 6 6-6" stroke="#fff" stroke-width="2.6" fill="none"/></svg></div>
  </div>

  <div class="abs card center" style="left:794px">
    <svg class="card-icon" width="70" height="70" viewBox="0 0 70 70" fill="none" stroke="#fff" stroke-width="2.4" stroke-linejoin="round">
      <circle cx="35" cy="35" r="6"/>
      <path d="M35 29c-6-8-4-24 6-24s10 14 0 22"/>
      <path d="M41 35c8-6 24-4 24 6s-14 10-22 0"/>
      <path d="M35 41c6 8 4 24-6 24s-10-14 0-22"/>
      <path d="M29 35c-8 6-24 4-24-6s14-10 22 0"/>
    </svg>
    <div class="card-title">AIR TREATMENT</div>
    <div class="card-text">Auis nostrud exercitation ullamco laboris nisi ut aliquip ex ea commodo consequat. Duis aute</div>
    <div class="card-arrow"><svg width="16" height="10" viewBox="0 0 16 10"><path d="M2 2l6 6 6-6" stroke="#fff" stroke-width="2.6" fill="none"/></svg></div>
  </div>
</section>

<section>
  <div class="abs quote-photo" role="img" aria-label="Photo of two white outdoor air conditioning units mounted on a wall"></div>
  <h2 class="abs sec-title quote-title">Request a quote</h2>
  <div class="abs underline quote-line"></div>
  <div class="abs field" style="top:2079px;height:43px">Name*</div>
  <div class="abs field" style="top:2136px;height:43px">E-mail*</div>
  <div class="abs field" style="top:2194px;height:43px">Telephone*</div>
  <div class="abs field area" style="top:2251px;height:108px">Write your message*</div>
  <div class="abs btn submit">Submit</div>
</section>

<section>
  <div class="abs contact-bg" role="img" aria-label="Faded photo of a technician servicing equipment"></div>
  <h2 class="abs sec-title contact-title">Contact us</h2>
  <div class="abs underline contact-line"></div>

  <svg class="abs info-icon" style="top:2688px" width="22" height="28" viewBox="0 0 22 28"><path fill="#2a8fc4" d="M11 0a11 11 0 0 0-11 11c0 8 11 17 11 17s11-9 11-17A11 11 0 0 0 11 0zm0 15a4 4 0 1 1 0-8 4 4 0 0 1 0 8z"/></svg>
  <div class="abs info" style="top:2684px">14 Rue des Tilleuls<br>38990 VALMORAY</div>

  <svg class="abs info-icon" style="top:2787px" width="22" height="22" viewBox="0 0 24 24"><path fill="#2a8fc4" d="M6.6 10.8a15.2 15.2 0 0 0 6.6 6.6l2.2-2.2a1 1 0 0 1 1-.25 11.4 11.4 0 0 0 3.6.57 1 1 0 0 1 1 1V20a1 1 0 0 1-1 1A17 17 0 0 1 3 4a1 1 0 0 1 1-1h3.5a1 1 0 0 1 1 1c0 1.25.2 2.45.57 3.57a1 1 0 0 1-.25 1z"/></svg>
  <div class="abs info" style="top:2771px">06 00 11 22 33<br>06 00 44 55 66</div>

  <svg class="abs info-icon" style="top:2880px" width="24" height="18" viewBox="0 0 24 18"><rect x="0" y="0" width="24" height="18" rx="2" fill="#2a8fc4"/><path d="M1 2l11 8 11-8" stroke="#fff" stroke-width="2" fill="none"/></svg>
  <div class="abs info" style="top:2874px">contact@climsolaris.fr</div>

  <div class="abs map" role="img" aria-label="Street map showing the company location"></div>
</section>

<footer>
  <svg class="abs footer" width="1200" height="284" viewBox="0 0 1200 284">
    <polygon points="60,110 600,10 1140,110 600,40" fill="#3ec88e"/>
    <polygon points="0,112 600,28 1200,112 1200,284 0,284" fill="#2c3a48"/>
  </svg>
  <div class="abs footer-logo center">ORV</div>
  <nav class="fnav">
    <a style="left:332px">HOME</a>
    <a style="left:474px">ABOUT</a>
    <a style="left:631px">SERVICES</a>
    <a style="left:813px">CONTACT US</a>
  </nav>
  <div class="abs copyright center">© Copyright 2020 . ORV . All Right Reserved</div>
  <div class="abs social first" style="left:541px"></div>
  <div class="abs social" style="left:578px"></div>
  <div class="abs social" style="left:615px"></div>
</footer>

</body>
</html>
```